Everything fresh, everything new

When I take over the practice, I would like to breathe new life into the practice. I want a business card design that catches the eye and brings a breath of fresh air

```html
<!DOCTYPE html>
<html lang="en">
<head>
<meta charset="utf-8">
<title>Vitalwerk – Business Card</title>
<link href="https://fonts.googleapis.com/css2?family=Poppins:wght@400;500;600;700&display=swap" rel="stylesheet">
<style>
  :root {
    --stage: #e6e6e4;
    --card-dark: #4a4a4c;
    --card-light: #ffffff;
    --brand-green: #8cc63f;
    --text-light: #ffffff;
    --text-dark: #444446;
  }
  * { margin: 0; padding: 0; box-sizing: border-box; }
  html, body {
    width: 1200px; height: 900px; overflow: hidden;
    background: var(--stage);
    font-family: "Poppins", sans-serif;
  }
  .canvas {
    position: relative; width: 1200px; height: 900px;
  }
  .card {
    position: absolute; left: 250px;
    width: 700px; height: 400px;
    border-radius: 24px; overflow: hidden;
    background: var(--card-dark);
    box-shadow: 0 10px 28px rgba(0,0,0,0.22);
  }
  .card--back { top: 40px; }
  .card--front { top: 460px; }

  /* Brand name block */
  .brand {
    position: absolute; display: flex; align-items: center; gap: 14px;
    font-weight: 600; letter-spacing: -0.5px; line-height: 1;
  }
  .brand__dot {
    width: 22px; height: 22px; border-radius: 50%;
  }
  .card--back .brand {
    left: 0; right: 0; top: 165px; justify-content: center;
    font-size: 66px; color: var(--text-light);
  }
  .card--back .brand__dot { background: var(--text-light); width: 28px; height: 28px; }

  .card__shape { position: absolute; inset: 0; width: 700px; height: 400px; }

  .card--front .brand {
    left: 380px; top: 178px;
    font-size: 44px; color: var(--text-dark);
  }
  .card--front .brand__dot { background: var(--brand-green); }

  /* Contact details */
  .contact { position: absolute; left: 52px; top: 100px; width: 215px; color: var(--text-light); }
  .contact__name {
    font-size: 25px; font-weight: 700; color: var(--brand-green);
    text-transform: uppercase; letter-spacing: -0.3px; line-height: 1.1;
    white-space: nowrap;
  }
  .contact__role { font-size: 18px; font-weight: 400; margin-top: 2px; }
  .contact__address {
    font-size: 16px; font-weight: 400; line-height: 1.45; margin-top: 32px; font-style: normal;
  }
  .contact__list { list-style: none; margin-top: 28px; }
  .contact__item {
    display: flex; align-items: center; gap: 12px;
    font-size: 16px; line-height: 1.7; white-space: nowrap;
  }
  .contact__icon { width: 15px; height: 15px; flex: none; }
</style>
</head>
<body>
<main class="canvas">

  <section class="card card--back" aria-label="Business card back">
    <div class="brand">
      <span class="brand__dot"></span>
      <span class="brand__name">Vitalwerk</span>
    </div>
  </section>

  <section class="card card--front" aria-label="Business card front">
    <svg class="card__shape" viewBox="0 0 700 400" aria-hidden="true">
      <path d="M296 0 C262 150 360 330 505 400 L700 400 L700 0 Z" fill="var(--card-light)"/>
      <path d="M306 0 C272 148 368 326 514 400 L522 400 C385 322 300 150 328 0 Z" fill="var(--brand-green)"/>
    </svg>

    <div class="brand">
      <span class="brand__dot"></span>
      <span class="brand__name">Vitalwerk</span>
    </div>

    <div class="contact">
      <h1 class="contact__name">Lena Hartmann</h1>
      <p class="contact__role">Director</p>
      <address class="contact__address">1042 Budapest, Fenyő utca<br>12. 2 floor 4.</address>
      <ul class="contact__list">
        <li class="contact__item">
          <svg class="contact__icon" viewBox="0 0 16 16" aria-hidden="true"><path d="M3.5 1.5 L6 4.5 L4.6 6.2 C5.5 8 7.8 10.4 9.8 11.4 L11.5 10 L14.5 12.5 L13 14.5 C7.5 14.5 1.5 8.5 1.5 3 Z" fill="var(--brand-green)"/></svg>
          <span>+36 30 555 0142</span>
        </li>
        <li class="contact__item">
          <svg class="contact__icon" viewBox="0 0 16 16" aria-hidden="true"><rect x="1" y="3" width="14" height="10" rx="1" fill="var(--brand-green)"/><path d="M1.5 3.5 L8 9 L14.5 3.5" fill="none" stroke="var(--card-dark)" stroke-width="1.3"/></svg>
          <span>hello@vitalwerk.hu</span>
        </li>
        <li class="contact__item">
          <svg class="contact__icon" viewBox="0 0 16 16" aria-hidden="true"><circle cx="8" cy="8" r="7" fill="var(--brand-green)"/><path d="M1 8 H15 M8 1 C4.5 5 4.5 11 8 15 M8 1 C11.5 5 11.5 11 8 15" fill="none" stroke="var(--card-dark)" stroke-width="1"/></svg>
          <span>www.vitalwerk.hu</span>
        </li>
      </ul>
    </div>
  </section>

</main>
</body>
</html>
```